Personal coach needs brochure design for inspirational essay about authenticity

Overview:
I want a beautiful brochure, 11”x17” that folds to 8-1/2”x11” with 4 pages. Think of it as an oversize greeting card.
• Front cover: photograph of a dancer and title with attribution of quote (Lumafold jpeg photo attached)
• Inside spread: Copy (Helena Brisk copy attached) with some appropriate illustration, based on cover photo
• Back cover: contact information, brief descriptive copy, two small photos (jpeg photo attached; see copy for direction)
Copy for front cover title, inside spread and back cover is attached in doc titled "Helena Brisk copy"

Purpose of brochure:
I'm a personal coach and once a year I produce a 4-page illustrated inspirational essay, which invites personal reflection on living a more mindful, meaningful life. Most people I send them to collect them. Someday in the future I'd like to put a collection of these essays into a coffee table book and also create a website for the collection, which is related to the personal coaching that I do.
I have the brochures printed hard copy. I have attached a few examples from previous years. Each has a unique design related to its theme.

Concept:
This year’s essay theme, “There will only ever be one you!” is based on a quote by Helena Brisk, a famous modern dancer. The complete quote, which appears in the copy, is about being true to one’s authentic self. The essay is not about dance, but because the author of the quote was a dancer who personified this theme of being unique to self, I have selected a photo of dance for the cover.

Design Guidance:
Front cover: One possibility is to expand the background color of the Lumafold photo so the photo seems to emerge from the background. But I am open to ideas. I think the photo is artsy enough as it is, but there may be other ways to treat it (e.g. special effects) that would also work. The title should appear somewhere. Make the attribution (--Helena Brisk) in smaller type than the title.

Inside Spread: There may be ways to borrow a design motif from the cover photo to make the inside spread more visually interesting, i.e., not just straight copy. I think it may be helpful to make the font size of the quote larger than the rest of the copy, but it has to be read in sequence. Or maybe it's printed in same size as copy, but then also repeated and displayed by itself in larger type.

Back cover: If you look at some of the other examples I’ve sent, you’ll see how the back cover is typically handled. I want a reduced version of the cover to be placed near the line that says "this is the 16th in a series.." Then, there’s a jpeg photo of Helena Brisk that should be placed next to the copy description of her.

Need extra days to review

```html
<!DOCTYPE html>
<html lang="en">
<head>
<meta charset="utf-8">
<title>There Will Only Ever Be One You – Brochure</title>
<link href="https://fonts.googleapis.com/css2?family=Cormorant+Upright:wght@400;500&family=Montserrat:ital,wght@0,400;0,600;0,700;1,400;1,600&display=swap" rel="stylesheet">
<style>
  :root {
    --ink: #060607;
    --slate: #9babb9;
    --slate-light: #b9c7d4;
    --slate-deep: #7f91a1;
    --paper-text: #f4f6f8;
    --stage: #e7e8ea;
    --smoke-1: #4a4d52;
    --smoke-2: #1a1b1e;
  }
  * { margin: 0; padding: 0; box-sizing: border-box; }
  html, body { width: 851px; height: 1200px; overflow: hidden; }
  body {
    background: var(--stage);
    font-family: "Montserrat", sans-serif;
    color: var(--paper-text);
    position: relative;
  }
  .spread {
    position: absolute;
    left: 25px;
    width: 800px;
    height: 518px;
    display: flex;
    box-shadow: 0 6px 18px rgba(0,0,0,.18);
  }
  .spread--outside { top: 45px; }
  .spread--inside { top: 625px; }
  .page { position: relative; width: 400px; height: 100%; overflow: hidden; }

  /* Back cover */
  .back-cover { background: var(--ink); padding: 36px 28px; }
  .back-intro { position: absolute; left: 28px; top: 38px; width: 200px; font-size: 6.4px; line-height: 1.45; }
  .back-intro em { font-weight: 600; }
  .contact { margin-top: 12px; }
  .contact a, .contact .value { color: var(--slate-light); text-decoration: none; }
  .series-thumb { position: absolute; left: 262px; top: 44px; width: 70px; text-align: center; }
  .series-thumb__frame { width: 70px; height: 88px; border: 1px solid #d8dde2; padding: 3px; }
  .series-thumb__art {
    width: 100%; height: 100%;
    background: radial-gradient(ellipse at 45% 35%, var(--smoke-1), var(--smoke-2) 60%, #000);
    position: relative;
  }
  .series-thumb__title { position: absolute; right: 5px; bottom: 12px; font-family: "Cormorant Upright", serif; font-size: 7px; line-height: .95; color: var(--slate-light); text-align: right; }
  .series-thumb__caption { margin-top: 6px; font-size: 6px; font-weight: 700; letter-spacing: .02em; }
  .series-thumb__caption span { display: block; font-family: "Cormorant Upright", serif; font-size: 11px; font-weight: 400; }
  .about { position: absolute; font-size: 5.2px; line-height: 1.45; }
  .about h3 { font-size: 7.4px; font-weight: 700; color: var(--slate-light); line-height: 1.15; margin-bottom: 4px; }
  .about--dancer { left: 28px; top: 196px; width: 340px; }
  .about--photographer { left: 150px; top: 318px; width: 220px; }
  .archive-photo { position: absolute; left: 28px; top: 330px; width: 104px; height: 86px; background: radial-gradient(ellipse at 55% 55%, #8d8a84, #2a2a2a 55%, #0b0b0b); }
  .archive-caption { position: absolute; left: 28px; top: 422px; width: 104px; font-size: 4.8px; line-height: 1.35; }

  /* Front cover */
  .front-cover {
    background:
      radial-gradient(ellipse 55% 45% at 48% 32%, #5d6168, transparent 70%),
      radial-gradient(ellipse 70% 60% at 40% 60%, #2c2e33, transparent 75%),
      var(--ink);
  }
  .cover-photo { position: absolute; left: 70px; top: 20px; width: 250px; height: 280px; }
  .cover-title { position: absolute; right: 34px; top: 330px; font-family: "Cormorant Upright", serif; line-height: .95; text-align: right; }
  .cover-title__line { display: block; font-size: 27px; color: var(--paper-text); }
  .cover-title__accent { color: var(--slate-light); font-size: 40px; }
  .cover-title__mixed { font-size: 27px; color: var(--paper-text); }
  .cover-attribution { position: absolute; right: 60px; top: 468px; font-size: 11px; font-weight: 600; }

  /* Inside spread */
  .inside-left { display: flex; }
  .essay-col { height: 100%; overflow: hidden; }
  .essay-col--dark { width: 170px; background: var(--ink); padding: 34px 14px 0 16px; font-size: 6.2px; line-height: 1.42; }
  .essay-col--dark p + p { margin-top: 7px; }
  .essay-lead { font-size: 8.2px; line-height: 1.25; color: var(--slate-light); font-weight: 600; margin-bottom: 2px; }
  .essay-lead--plain { color: var(--paper-text); font-weight: 400; }
  .essay-col--slate { width: 230px; background: var(--slate); padding: 44px 26px 0 22px; font-size: 11px; line-height: 1.3; }
  .essay-col--slate strong { font-size: 13px; font-weight: 700; }
  .inside-right { background: var(--slate); }
  .inside-right::before { content: ""; position: absolute; left: 0; top: 0; bottom: 0; width: 10px; background: linear-gradient(90deg, rgba(0,0,0,.08), transparent); }
  .line-dancer { position: absolute; left: 22px; top: 50px; width: 130px; height: 290px; }
  .pull-quote { position: absolute; left: 150px; top: 38px; width: 225px; font-size: 9px; line-height: 1.25; text-align: center; }
  .closing { position: absolute; left: 22px; top: 392px; width: 360px; font-size: 6.2px; line-height: 1.45; }
</style>
</head>
<body>

<section class="spread spread--outside" aria-label="Outside spread">
  <div class="page back-cover">
    <div class="back-intro">
      <p><em>There Will Only Ever Be One You</em> is the 16th in a series of Labor Day essays inviting a moment of reflection on living a more meaningful, more mindful life</p>
      <p class="contact">Nora Vell Ashby, Ph.D.<br>Heron Hill House<br>18 Orchard Lane<br>Eastfield, Vermont 05401</p>
      <p class="contact">Mobile: <span class="value">555-014-2290</span><br>Email: <a href="mailto:nora@ashbycoach.net">nora@ashbycoach.net</a></p>
    </div>

    <div class="series-thumb">
      <div class="series-thumb__frame">
        <div class="series-thumb__art" role="img" aria-label="Reduced front cover: dancer leaping through dark smoke">
          <span class="series-thumb__title">There will<br>Only Ever be<br>One You</span>
        </div>
      </div>
      <p class="series-thumb__caption">THE 16TH IN A <span>Series..</span></p>
    </div>

    <div class="about about--dancer">
      <h3>About<br>Helena Brisk:</h3>
      <p>Born in 1894, Helena Brisk danced and taught for over 70 years. She is recognized as a primal artistic force of the 20th century, whose influence on modernity has been compared to Aldo Ferrant, Owen Hale, Ilya Marek, and Silas Dorne. Her themes dealt with the lives and conflicts of ordinary people, and she brought serious issues to the stage like war, poverty, intolerance and the injustices of slavery and treatment of Native Americans. Rebelling against conventions of the past, her dancing and choreography exposed the depths of human emotion through intense movements that were forceful, stark, angular, jagged, and percussive – startlingly unlike the formality of classical ballet, which she saw as antiquated.</p>
    </div>

    <div class="archive-photo" role="img" aria-label="Archive photograph of the dancer in a flowing pale gown"></div>
    <p class="archive-caption">"Helena Brisk in Letter to the World, No. 1" © The Ruth Calder Archive</p>

    <div class="about about--photographer">
      <h3>About Photographer<br>Ruth Calder:</h3>
      <p>In 1935 Ruth Calder saw a performance by modern dancer and choreographer Helena Brisk. Calder was so inspired by the dance performance that she introduced herself to Brisk, and the two artists began an artistic collaboration that lasted more than 60 years. Calder often photographed dancers in action, to capture the emotion behind their movement. Her artistic style was in line with Brisk's philosophy of dance. This photo from the dance, "Letter to the World," is one of Calder's most famous photographs. The title of this work comes from an Ada Whitlow poem, which inspired Brisk to create a dance performance based on Whitlow's life.</p>
    </div>
  </div>

  <div class="page front-cover">
    <div class="cover-photo" role="img" aria-label="Photograph of a barefoot dancer in a flowing dark dress leaping through a cloud of smoke"></div>
    <h1 class="cover-title">
      <span class="cover-title__line">There will</span>
      <span class="cover-title__line"><span class="cover-title__accent">Only</span> <span class="cover-title__mixed">Ever be</span></span>
      <span class="cover-title__line cover-title__accent">One You</span>
    </h1>
    <p class="cover-attribution">– Helena Brisk</p>
  </div>
</section>

<section class="spread spread--inside" aria-label="Inside spread">
  <div class="page inside-left">
    <div class="essay-col essay-col--dark">
      <p><span class="essay-lead essay-lead--plain">In the rural Ohio village where I grew up, one of the highlights of Sunday morning church service --</span> in between congregational hymn-singing and the preacher's sermon -- was the "special selection," a musical performance by a parishioner. Typically, it was a vocalist or instrumental on piano, organ or violin. One Sunday, we were surprised by an unusual performance. A plump, buxom farm wife approached the pulpit, puckered up her lips and unexpectedly began to whistle the hymn <em>"The Old Rugged Cross."</em> As a 10-year-old, I found this hilarious as I tried to choke back my wide-eyed amazement and giggles.</p>
      <p>Despite the irreverence of my pre-adolescent reaction, this memory has stayed with me for decades as an iconic example of the wonderment of individual differences. Of the delight I find in witnessing someone express herself in sometimes surprising and even courageous ways. Of the marvel of beholding a person be truly authentic and uniquely original.</p>
      <p><span class="essay-lead">Someone who personified the irrepressible impulse to express her individuality was the early 20th century dancer and choreographer Helena Brisk.</span> A pioneer of modern dance, she threw tradition overboard and was inspired to dance in a way that was a radical departure from the formalized style and rigidly dictated forms of classical ballet. Brisk felt compelled to express the rawness and emotion of human experience in her dancing -- not just present a form of pretty entertainment. Iconoclastically brilliant, she created a new language of dance, a revolutionary vocabulary of movement that electrified the stage, often creating a visceral response in the audience.</p>
    </div>
    <div class="essay-col essay-col--slate">
      <p><strong>In her biography of Brisk,</strong> her friend and equally talented choreographer Clara Voss recalled that despite sensational reviews for her own innovative work in the Broadway musical Prairie Song!, Voss had a gnawing feeling that her work was only mediocre. Voss confessed her anxieties to Brisk who listened quietly and then responded, "There will only ever be one you!" Continuing, she added:</p>
    </div>
  </div>

  <div class="page inside-right">
    <div class="line-dancer" role="img" aria-label="Line illustration of a dancer leaping in a billowing white skirt, arms raised"
         style="background: radial-gradient(ellipse 45% 40% at 45% 55%, #f1f3f5, #dfe5ea 60%, transparent 75%);"></div>
    <blockquote class="pull-quote">"There is a vitality, a life-force, an energy, a quickening that is translated through you into action. And because there is only one of you in all of time, this expression is unique. And if you block it, the world will not have it. It is not your business to determine how good it is nor how valuable nor how it compares with other expressions. It is your business to keep it yours clearly and directly, to keep the channel open. You have to keep open and aware directly to the urges that motivate you. Above all else, keep the channel open!"</blockquote>
    <p class="closing">Brisk's wisdom reminds us that we must not hold back or judge our gifts. Although there may be moments when we doubt ourselves or when we worry that we're not good enough, our job is to be fearless and to "keep the channel open." Guard the precious miracle of your own uniqueness. Find that home-sweet-home feeling where you feel you are your most authentic self. There will only ever be one you! And importantly, respect the differences of others. Our world would be a drab, boring place if we all only whistled one tune.</p>
  </div>
</section>

</body>
</html>
```